Business card design only (Have Logo Online) Shoudl be quick and easy for designer

We would like to have a business card design that is in-line with our company logo. Final deliverables should include two EPS extension file. One for the front card design and the other the back-end design. Please also indicate the font style used.

Advisory Pebbles is a social enterprise that focuses on utilizing technology, unique methodologies and international partnerships to provide a one-stop location for economical and dependable IT-related solutions.

Target Market(s)

Micro, small and medium business owners.

Industry/Entity Type

Business

Requirements
Must have
• The business card should incorporate our company logo.
Nice to have
• A little web 2.0 style would be nice but I haven''t decided yet.

```html
<!DOCTYPE html>
<html lang="en">
<head>
<meta charset="utf-8">
<title>Advisory Pebbles – Business Card Concepts</title>
<link href="https://fonts.googleapis.com/css2?family=Caveat:wght@500&family=Open+Sans:ital,wght@0,400;0,700;0,800;1,400&display=swap" rel="stylesheet">
<style>
  :root {
    --page: #ffffff;
    --mint-bg: #e6f8dc;
    --lime-panel: #c4fb92;
    --aqua-bg: #e7fbf4;
    --aqua-panel: #c6fde3;
    --cream-bg: #f7f5e2;
    --yellow-panel: #f6f46d;
    --leaf: #3fb72f;
    --soft-leaf: #bdf77c;
    --faint-leaf: #dff5c0;
    --ink: #111a14;
    --shadow: rgba(0,0,0,0.45);
  }
  * { margin: 0; padding: 0; box-sizing: border-box; }
  html, body { width: 1200px; height: 1055px; overflow: hidden; background: var(--page); }
  .sheet { position: relative; width: 1200px; height: 1055px; }

  .card {
    position: absolute;
    width: 552px; height: 314px;
    overflow: hidden;
    box-shadow: 2px 2px 2px var(--shadow);
  }
  .col-left { left: 38px; }
  .col-right { left: 613px; }
  .row-1 { top: 25px; }
  .row-2 { top: 366px; }
  .row-3 { top: 709px; }

  .bg-mint { background: var(--mint-bg); }
  .bg-aqua { background: var(--aqua-bg); }
  .bg-cream { background: var(--cream-bg); }

  .side-panel { position: absolute; top: 0; right: 0; width: 203px; height: 100%; }
  .side-panel.lime { background: var(--lime-panel); }
  .side-panel.aqua { background: var(--aqua-panel); }
  .side-panel.yellow { background: var(--yellow-panel); }
  .curved-panel { position: absolute; top: 0; left: 0; }

  .brand {
    position: absolute; left: 34px; top: 178px;
    display: flex; align-items: center; gap: 12px;
  }
  .brand-dot {
    width: 46px; height: 46px; border-radius: 50%;
    background: var(--leaf);
    flex: none;
  }
  .brand-name {
    font-family: "Open Sans", sans-serif;
    font-weight: 800;
    font-size: 42px;
    line-height: 1;
    letter-spacing: -0.5px;
    color: var(--leaf);
    white-space: nowrap;
  }

  .tagline {
    position: absolute; left: 0; width: 100%;
    top: 252px; text-align: center;
    font-family: "Caveat", cursive;
    font-weight: 500;
    font-size: 28px;
    line-height: 1.1;
    color: var(--ink);
    white-space: nowrap;
  }
  .motto {
    position: absolute; right: 10px; top: 10px;
    font-family: "Caveat", cursive;
    font-weight: 500;
    font-size: 31px;
    color: var(--ink);
    white-space: nowrap;
  }

  .back-ornament {
    position: absolute; left: -190px; top: -30px;
    width: 480px; height: 480px; border-radius: 50%;
    background: var(--faint-leaf);
  }
  .contact {
    position: absolute; right: 22px; top: 20px;
    text-align: right;
    font-family: "Open Sans", sans-serif;
    color: var(--ink);
  }
  .contact-name { font-size: 29px; font-weight: 700; color: var(--leaf); line-height: 1.1; }
  .contact-role { font-size: 16px; font-style: italic; margin-right: 72px; line-height: 1.1; }
  .contact-address { margin-top: 28px; font-size: 20px; line-height: 29px; }
  .contact-lines { margin-top: 24px; font-size: 19.5px; line-height: 27px; }
</style>
</head>
<body>
<main class="sheet">

  <section class="card bg-mint col-left row-1">
    <div class="brand"><span class="brand-dot"></span><span class="brand-name">Advisory Pebbles</span></div>
    <p class="tagline">Delivering affordable, simple and innovative results!</p>
  </section>

  <section class="card bg-mint col-right row-1">
    <div class="side-panel lime"></div>
    <p class="motto">Growing with you!</p>
    <div class="brand"><span class="brand-dot"></span><span class="brand-name">Advisory Pebbles</span></div>
  </section>

  <section class="card bg-mint col-left row-2">
    <svg class="curved-panel" width="552" height="314" viewBox="0 0 552 314" aria-hidden="true">
      <path d="M354 0 H534 Q550 80 548 157 Q546 250 536 314 H354 Z" fill="var(--lime-panel)"/>
    </svg>
    <div class="brand"><span class="brand-dot"></span><span class="brand-name">Advisory Pebbles</span></div>
  </section>

  <section class="card bg-aqua col-right row-2">
    <div class="side-panel aqua"></div>
    <div class="brand"><span class="brand-dot"></span><span class="brand-name">Advisory Pebbles</span></div>
    <p class="tagline">Delivering affordable, simple and innovative results!</p>
  </section>

  <section class="card bg-cream col-left row-3">
    <div class="back-ornament"></div>
    <div class="contact">
      <p class="contact-name">Lena Marwick</p>
      <p class="contact-role">Founder</p>
      <p class="contact-address">2184 Alder Lane<br>BC Canada<br>V3K 2P7</p>
      <p class="contact-lines">Cell: 1-604-555-0148<br>E-mail: lena.marwick@advisorypebbles.com<br>www.advisorypebbles.com</p>
    </div>
  </section>

  <section class="card bg-cream col-right row-3">
    <div class="side-panel yellow"></div>
    <p class="motto">Growing with you!</p>
    <div class="brand"><span class="brand-dot"></span><span class="brand-name">Advisory Pebbles</span></div>
  </section>

</main>
</body>
</html>
```